Tea bag packaging design for KELVIRA

Hello. I am creating a green tea and soybean tea, and I am looking for packaging designs. I will attach some designs I like and our current KELVIRA logo. Feel free to follow the designs or create something of your own.

Package size is 200 (W) x 290(L) mm

The package is a white aluminum package so it can accommodate a wide range of colors. We don't want to pay a ton in printing so 5 colors or less is nice. But we will make exceptions for something more colorful if it's well done.

Target Market(s)

Women and Men in 30s-40s

Industry/Entity Type

food and beverage

Font styles to use
Sans Serif
Other font styles liked:
• red hat is the font of the logo

Requirements
Must have
• clean, simple, but bold design
Nice to have
• images of soybeans and green tea leaves on the package

```html
<!DOCTYPE html>
<html lang="en">
<head>
<meta charset="utf-8">
<title>KELVIRA Tea Leaf and Soybean – Front Label</title>
<link href="https://fonts.googleapis.com/css2?family=Red+Hat+Display:wght@700;800;900&display=swap" rel="stylesheet">
<style>
  :root {
    --stage: #d6d6d6;
    --leaf-green: #8dc63f;
    --deep-green: #67a03f;
    --badge-green: #6a9a48;
    --cream: #eef2bc;
    --cream-soft: #f1f4c6;
    --lime: #b9d957;
    --ink-green: #5e8d3d;
    --brand-ink: #1d1d1b;
    --white: #ffffff;
    --dot: #f2f7c8;
    --bean: #d8b68c;
    --bean-dark: #c29467;
  }
  * { box-sizing: border-box; margin: 0; padding: 0; }
  html, body { width: 1200px; height: 1117px; overflow: hidden; }
  body {
    background: var(--stage);
    font-family: "Red Hat Display", "Helvetica Neue", Arial, sans-serif;
    position: relative;
  }
  .label {
    position: absolute;
    left: 255px; top: 58px;
    width: 690px; height: 1000px;
    background: var(--leaf-green);
    overflow: hidden;
  }
  .sparkles { position: absolute; inset: 0; }
  .brand {
    position: absolute; left: 0; right: 0; top: 248px;
    text-align: center;
  }
  .brand-name {
    font-weight: 800; font-size: 23px; letter-spacing: 0.3px; line-height: 1;
    color: var(--brand-ink);
  }
  .title {
    position: absolute; left: 86px; top: 304px;
    font-weight: 900; font-size: 86px; line-height: 1;
    letter-spacing: 1px; color: var(--white);
  }
  .subtitle {
    position: absolute; left: 92px; top: 394px;
    font-weight: 800; font-size: 35px; line-height: 1;
    color: var(--white);
  }
  .leaf-pattern {
    position: absolute; left: 300px; top: 440px;
    width: 390px; height: 381px;
    background: linear-gradient(165deg, var(--cream-soft) 0%, var(--lime) 50%, var(--deep-green) 100%);
    border-top-left-radius: 260px 320px;
  }
  .organic-badge {
    position: absolute; left: 66px; top: 440px;
    width: 162px; height: 162px; border-radius: 50%;
    background: var(--badge-green);
    display: flex; flex-direction: column; align-items: center; justify-content: center;
    line-height: 0.95;
  }
  .organic-badge .pct { font-weight: 800; font-size: 37px; color: var(--cream); }
  .organic-badge .pure { font-weight: 900; font-size: 37px; color: var(--white); }
  .organic-badge .org { font-weight: 800; font-size: 21px; color: var(--white); }
  .base-band {
    position: absolute; left: 0; right: 0; top: 821px; bottom: 0;
    background: var(--cream);
  }
  .product-photo {
    position: absolute; left: 195px; top: 600px;
    width: 300px; height: 312px;
    border-radius: 150px 150px 140px 140px;
    background: radial-gradient(ellipse at 55% 70%, var(--bean) 0%, var(--bean-dark) 55%, var(--deep-green) 100%);
  }
  .claim {
    position: absolute; top: 850px;
    width: 120px; text-align: center;
    color: var(--ink-green);
  }
  .claim svg { display: block; margin: 0 auto; }
  .claim-text { font-weight: 800; font-size: 15px; line-height: 1; margin-top: 12px; }
  .claim.gluten { left: 81px; }
  .claim.gmo { left: 501px; }
  .net-weight {
    position: absolute; left: 0; right: 0; top: 940px;
    text-align: center; line-height: 1;
    font-weight: 800; font-size: 17px; color: var(--ink-green);
  }
</style>
</head>
<body>
  <section class="label" aria-label="KELVIRA front label">
    <svg class="sparkles" width="690" height="1000" aria-hidden="true">
      <g fill="var(--dot)">
        <circle cx="247" cy="105" r="6"/>
        <circle cx="90" cy="144" r="3"/>
        <circle cx="195" cy="188" r="3"/>
        <circle cx="542" cy="131" r="3"/>
        <circle cx="84" cy="229" r="8"/>
        <circle cx="608" cy="221" r="7"/>
        <circle cx="225" cy="282" r="3"/>
        <circle cx="487" cy="267" r="3"/>
      </g>
    </svg>

    <div class="brand"><span class="brand-name">KELVIRA</span></div>

    <h1 class="title">KELVIRA</h1>
    <p class="subtitle">TEA LEAF AND SOYBEAN</p>

    <div class="leaf-pattern" role="img" aria-label="Large stylised tea leaf pattern in cream and green tones"></div>

    <div class="base-band"></div>

    <div class="product-photo" role="img" aria-label="Photo of a wooden spoon full of soybeans with fresh green tea leaves"></div>

    <div class="organic-badge">
      <span class="pct">100%</span>
      <span class="pure">PURE</span>
      <span class="org">ORGANIC</span>
    </div>

    <div class="claim gluten">
      <svg width="78" height="78" viewBox="0 0 78 78" aria-hidden="true">
        <g fill="none" stroke="var(--ink-green)" stroke-width="3" stroke-linecap="round">
          <circle cx="39" cy="39" r="36"/>
          <line x1="14" y1="64" x2="64" y2="14"/>
          <line x1="39" y1="20" x2="39" y2="60"/>
          <path d="M39 24c-4 3-4 8 0 11c4-3 4-8 0-11z"/>
          <path d="M39 38c-8-1-12 2-12 8c7 1 11-2 12-8z"/>
          <path d="M39 38c8-1 12 2 12 8c-7 1-11-2-12-8z"/>
          <path d="M39 48c-8-1-12 2-12 8c7 1 11-2 12-8z"/>
          <path d="M39 48c8-1 12 2 12 8c-7 1-11-2-12-8z"/>
        </g>
      </svg>
      <div class="claim-text">GLUTEN FREE</div>
    </div>

    <p class="net-weight">NET WT 10 OZ (283 G)</p>

    <div class="claim gmo">
      <svg width="78" height="78" viewBox="0 0 78 78" aria-hidden="true">
        <g fill="none" stroke="var(--ink-green)" stroke-width="3" stroke-linecap="round">
          <circle cx="39" cy="39" r="36"/>
          <line x1="14" y1="64" x2="64" y2="14"/>
        </g>
        <text x="39" y="47" text-anchor="middle" font-family="Red Hat Display, sans-serif" font-weight="800" font-size="22" fill="none" stroke="var(--ink-green)" stroke-width="1.6">GMO</text>
      </svg>
      <div class="claim-text">NON GMO</div>
    </div>
  </section>
</body>
</html>
```